Salt Under Canvas: Years of Quiet Marching

I am an independent author writing a book about my life in the military while serving under the Don't Ask, Don't Tell Policy. The book will be published in both print and E-book format. For the print book, the front cover should be military dog tags with the main title printed on the tags while the subtitle printed at the top. The bottom portion of the front cover should have my name, "Bernard L. Whitfield". For the spine, the main title and my name should appear. The back will be reserved for the book's teaser as well as web contact information, both of which I will provide at a later time (still in development). The E-book cover can simply be the same as the front cover design for the print book.
Updates

Update! Change of heart on the positioning of the main title and the subtitle. Prefer the main title above the subtitle.

Thanks for all the submissions thus far.  Lots to choose from!  I finally have some info for the back covers.  If you have time, could you include the following on the back.

An unapologetic, first-hand account of life under Don’t Ask, Don’t Tell (make sure this is in big bold print at top)

(This is the teaser to be placed under) From 1993 to 2011, the Don’t Ask, Don’t Tell Policy affected the way LGBT military personnel not only interacted with people in public, but among each other in private.  From using code words in public to engaging in a secret sex life in private, the policy created a ridiculous social construct under which LGBT military personnel were expected to adhere.  For six and a half years, the author lived under these rules with the help of love-interests, friends, and allied co-workers.  Salt Under Canvas recalls episodes of the author living life to the fullest while covering his tracks just enough to avoid getting caught.  Despite enduring injustice, the author demonstrates just how resilient the LGBT community actually was.  Whether it was secret gatherings, a disciplined code of silence, or simply looking out for each other, Salt Under Canvas seeks to tell the story few have a guts to admit: how LGBT personnel got around the rules of Don’t Ask, Don’t Tell in order to maintain some sense of dignity

(The following contact info is to be placed toward the bottom centered.  Leave enough space to still place an ISBN)

www.facebook.com/saltcanvasbook           www.salt-canvas.com              www.twitter.com/saltcanvasbook

Hi Designers!

Lots of wonderful submissions that I appreciate very much.  Just an FYI, I intend to publish the print book cover via Print Harbor.  The instructions for book covers is found via the following link:

The design that I go with will need to adhere to these specifications.  No worries if your does not comply with these parameters at the time being.  I have every intention of offering payment for additional revisions to the covers.  Please send me quotes for additional revisions once the contest is over.  Also, to the design I pick, I will also require an E-book avatar, but we can discuss this later.

Target Market(s)

Target audience for this book are LGBT 25 and older, and women 25 and older

Requirements
Must have
• Dog Tags with main title printed on it.
Nice to have
• Print book and the E-book are going to have the same design, so try to ensure that the front cover design can catch attention as a thumbnail on a webpage.

```html
<!DOCTYPE html>
<html lang="en">
<head>
<meta charset="utf-8">
<title>Salt Under Canvas: Years of Quiet Marching — Front Cover</title>
<link rel="stylesheet" href="https://fonts.googleapis.com/css2?family=Courier+Prime:wght@700&family=Stardos+Stencil:wght@700&family=Arimo:wght@700&display=swap">
<style>
  :root {
    --page-bg: #ffffff;
    --field-light: #c9d7aa;
    --field-mid: #a9bb82;
    --field-dark: #6f8450;
    --tag-light: #6e7173;
    --tag-mid: #4a4d50;
    --tag-dark: #2e3133;
    --tag-rim: #b9bcbe;
    --title-ink: #ffffff;
    --title-edge: #1d1f21;
    --stencil-ink: #5b6b44;
    --wire-ink: rgba(70, 88, 50, 0.35);
    --grenade-fill: #3d4a33;
    --author-ink: #ffffff;
  }
  * { margin: 0; padding: 0; box-sizing: border-box; }
  html, body {
    width: 1200px; height: 985px; overflow: hidden;
    background: var(--page-bg);
  }
  .cover {
    position: absolute; left: 282px; top: 0;
    width: 636px; height: 985px; overflow: hidden;
    background:
      radial-gradient(ellipse at 50% 45%, var(--field-light) 0%, var(--field-mid) 55%, var(--field-dark) 100%);
  }
  .wire {
    position: absolute; left: 0; top: 520px; width: 636px; height: 280px;
  }
  .tag {
    position: absolute; width: 610px; height: 300px;
    border-radius: 70px / 90px;
    border: 7px solid var(--tag-rim);
    transform: rotate(11deg);
  }
  .tag--back {
    left: -10px; top: 150px;
    background: linear-gradient(160deg, var(--tag-mid), var(--tag-dark));
    box-shadow: 0 14px 28px rgba(0,0,0,0.45);
  }
  .tag--front {
    left: 12px; top: 60px;
    background: linear-gradient(150deg, var(--tag-light) 0%, var(--tag-mid) 55%, var(--tag-dark) 100%);
    box-shadow: 0 14px 30px rgba(0,0,0,0.5);
  }
  .tag__ring {
    position: absolute; left: 14px; top: 112px;
    width: 36px; height: 36px; border-radius: 50%;
    border: 5px solid var(--tag-rim);
    background: var(--tag-dark);
  }
  .title {
    position: absolute; left: 72px; top: 38px;
    font-family: "Courier Prime", "Courier New", monospace;
    font-weight: 700; color: var(--title-ink);
    font-size: 42px; line-height: 1.18;
    text-shadow:
      -2px -2px 0 var(--title-edge), 2px -2px 0 var(--title-edge),
      -2px 2px 0 var(--title-edge), 2px 2px 0 var(--title-edge),
      3px 4px 4px rgba(0,0,0,0.6);
  }
  .title__main { display: block; letter-spacing: 1px; }
  .title__sub { display: block; }
  .policy {
    position: absolute; left: 0; width: 636px; top: 540px;
    text-align: center;
    font-family: "Stardos Stencil", "Arial Black", sans-serif;
    font-weight: 700; font-variant: small-caps;
    color: var(--stencil-ink);
    font-size: 58px; line-height: 1.1;
  }
  .grenade {
    position: absolute; left: 505px; top: 705px;
    width: 118px; height: 285px;
    border-radius: 50px 50px 40px 40px;
    background: linear-gradient(90deg, #2b3524, var(--grenade-fill) 45%, #26301f);
    opacity: 0.85;
  }
  .author {
    position: absolute; left: 0; width: 636px; top: 924px;
    text-align: center;
    font-family: "Arimo", Arial, sans-serif;
    font-weight: 700; font-size: 31px;
    color: var(--author-ink);
  }
</style>
</head>
<body>
  <main class="cover">
    <svg class="wire" viewBox="0 0 636 280" aria-hidden="true">
      <line x1="0" y1="38" x2="636" y2="30" stroke="var(--wire-ink)" stroke-width="3"/>
      <line x1="0" y1="88" x2="636" y2="84" stroke="var(--wire-ink)" stroke-width="3"/>
      <line x1="0" y1="180" x2="636" y2="176" stroke="var(--wire-ink)" stroke-width="3"/>
      <line x1="0" y1="244" x2="636" y2="236" stroke="var(--wire-ink)" stroke-width="3"/>
    </svg>

    <div class="tag tag--back" role="img" aria-label="Second military dog tag behind the first"></div>
    <div class="tag tag--front" role="img" aria-label="Military dog tag stamped with the book title">
      <span class="tag__ring"></span>
      <h1 class="title">
        <span class="title__main">SALT UNDER CANVAS:</span>
        <span class="title__sub">Years of Quiet</span>
        <span class="title__sub">Marching</span>
      </h1>
    </div>

    <p class="policy">Don't Ask,<br>Don't Tell Policy</p>

    <div class="grenade" role="img" aria-label="Hand grenade silhouette"></div>

    <p class="author">Bernard L. Whitfield</p>
  </main>
</body>
</html>
```